Australian Careers Business Needs 2 Banner Ad Design

We need a banner ad design for a new company based in Australia called Bright Sparrows. We provide career tools and insights to young professionals. Our target market is 20-30 year olds.

We would like to see designs that attract users on the site to click on the banner and sign up for a weekly newsletter. The newsletter will feature a blog, cheat sheets etc. Inspiration in their inbox!

The second banner is to attract users to sign up for a Horizon Summit. They would click on it to find out more information and then register with their email address. This convention is a 1 day workshop designed to enhance young professionals abilities to give their best at work. There will CEO insights etc.

Use of images or flash is ok. Needs to look very professional and presented in accordance to the current colour scheme in place. Visit http://www.brightsparrows-demo.com/home to understand.

Banner sizes 300 x 250.
Mandatory use of Corporate Colours required on Font.
R66 G73 B74
R242 G240 B230
R38 G128 B138

No logo necessary.

Project Deadline Extended Reason: I made an error in selecting 2 days and meant to select 5 days. Please can I amend now without the charge as its instantly after submitting the project. I am about to close out 3 existing projects and this is the second one I've just loaded today.Hence i intend to continue repeat business.Thanks,Megan Added Wednesday, April 1, 2015

Hi All,As both banners will feature on the Bright Sparrows site there is no need for a logo or hyperlink to the site.I would like to see some better images, and a bit more creative flair.Please don't use single female images as I am wanting to avoid the women in business perception. We cater to young professionals.Some suggestions for lines to utilise on the newsletter ad:Click here for weekly career tipsInvest in your career for free hereJoin the weekly conversationWeekly career tips in your inboxSign up for our weekly newsletterSome suggestions for lines to use on the horizon summit ad:Register for the Horizon Summit - Find out how to get ahead of your peersAre you a millennial climbing the corporate ladder? Find out how to rise to the topInterested in hearing from experts who recognise millennials are our future business leaders? Click here.Thanks,Megan Added Friday, April 3, 2015

Project Deadline Extended Reason: I need to extend deadline as the designs submitted are not what I was seeking. Added Saturday, April 4, 2015

Target Market(s)

20-30 years

Industry/Entity Type

Business

Font styles to use
Sans Serif

Requirements
Must have
• Please use images in the attached as options
Should not have
• NO LOGO - Its already onsite so not needed.

```html
<!DOCTYPE html>
<html lang="en">
<head>
<meta charset="utf-8">
<title>Bright Sparrows – Banner Ads</title>
<link rel="stylesheet" href="https://fonts.googleapis.com/css2?family=Arimo:wght@400;700&display=swap">
<style>
  :root {
    --ink: #42494a;
    --ink-soft: #5f6566;
    --cream: #f2f0e6;
    --teal: #26808a;
    --teal-deep: #1f6f78;
    --sky: #8ec9d6;
    --sky-deep: #3f97ab;
    --orange-top: #fbb04a;
    --orange-bottom: #e2621a;
    --cocoa: #5a2c0e;
    --label-red: #d90000;
    --page: #ffffff;
  }
  * { box-sizing: border-box; margin: 0; padding: 0; }
  html, body { width: 1200px; height: 1200px; overflow: hidden; background: var(--page); }
  body { font-family: "Arimo", Arial, sans-serif; }

  .board {
    position: absolute; left: 0; top: 0;
    width: 850px; height: 850px;
    transform: scale(1.41176);
    transform-origin: 0 0;
  }

  .caption { position: absolute; font-size: 21px; line-height: 1; white-space: nowrap; transform: translateX(-50%); }
  .caption--red { color: var(--label-red); }
  .caption--dark { color: #111; }

  .banner {
    position: absolute; width: 300px; height: 250px;
    background: linear-gradient(180deg, var(--teal) 0%, var(--teal-deep) 100%);
    border: 1px solid #3b6d72;
    overflow: hidden;
  }
  .banner__top { position: absolute; left: 0; top: 0; width: 300px; height: 72px; }
  .banner__heading {
    position: absolute; left: 0; right: 0; top: 14px;
    text-align: center; font-weight: 700; font-size: 18.5px; color: var(--ink);
    letter-spacing: 0.1px;
  }
  .banner__heading--teal { color: var(--teal); font-size: 21px; top: 12px; }

  .panel {
    position: absolute; left: 10px; top: 56px; width: 280px; height: 136px;
    border: 1px solid rgba(255,255,255,0.55);
    border-radius: 0 0 7px 7px; overflow: hidden;
    box-shadow: 0 1px 3px rgba(0,0,0,0.25);
  }
  .panel__feature {
    position: absolute; left: 0; top: 0; width: 100%; height: 86px;
    background: radial-gradient(ellipse at 45% 60%, #fbfaf4 0%, var(--cream) 55%, #d9d8cf 100%);
  }
  .panel__strip {
    position: absolute; left: 0; top: 86px; width: 100%; height: 50px;
    background: radial-gradient(ellipse at 50% 30%, #d4eef3 0%, var(--sky) 45%, var(--sky-deep) 100%);
  }
  .thumb {
    position: absolute; left: 9px; top: 4px; width: 62px; height: 62px;
    background: #fff; border: 1px solid #9a9a94; padding: 3px;
  }
  .thumb__fill { width: 100%; height: 100%; }
  .thumb__fill--watch { background: linear-gradient(135deg, #d8d2c8, #6f6a66 55%, #2f2c2c); }
  .thumb__fill--phone { background: linear-gradient(160deg, #e8e4dc, #3a3a3e 55%, #1f1f22); }
  .thumb__fill--typing { background: linear-gradient(135deg, #dfe6ea, #8fa9bb 55%, #5d7487); }
  .thumb__fill--crowd { background: linear-gradient(160deg, #c8cdd4, #4b5a6e 50%, #1f2836); }

  .headline {
    position: absolute; left: 80px; top: 14px; width: 196px;
    font-weight: 700; font-size: 19px; line-height: 19px; color: var(--ink-soft);
  }
  .headline--three { left: 92px; top: 14px; }
  .headline--four { left: 92px; top: 6px; }
  .lead {
    position: absolute; left: 75px; top: 10px; width: 205px;
    font-size: 15px; line-height: 18px; color: var(--ink);
  }

  .email-field {
    position: absolute; left: 52px; top: 12px; width: 176px; height: 25px;
    background: #fff; border: 1px solid #5a5f60;
    font-size: 11.5px; line-height: 23px; padding-left: 9px; color: #555;
  }
  .strip-title {
    position: absolute; left: 0; right: 0; top: 9px;
    text-align: center; color: #fff; font-weight: 700; font-size: 19.5px; line-height: 19px;
    text-shadow: 0 1px 2px rgba(0,0,0,0.45);
  }

  .cta {
    position: absolute; top: 203px; width: 139px; height: 37px;
    background: linear-gradient(180deg, var(--orange-top) 0%, #f28a2a 50%, var(--orange-bottom) 100%);
    border-radius: 3px; box-shadow: 0 3px 5px rgba(0,0,0,0.35);
    color: #fff; font-weight: 700; font-size: 13px;
  }
  .cta__label {
    position: absolute; left: 0; top: 0; width: 102px; height: 37px;
    line-height: 37px; text-align: center;
    text-shadow: 0 1px 1px rgba(90,40,10,0.8);
  }
  .cta__divider { position: absolute; left: 102px; top: 2px; width: 1px; height: 33px; background: rgba(140,60,10,0.55); box-shadow: 1px 0 0 rgba(255,220,170,0.5); }
  .cta__icon { position: absolute; left: 108px; top: 5px; width: 27px; height: 27px; }
</style>
</head>
<body>
<main class="board">

  <p class="caption caption--red" style="left:271px; top:22px;">Banner 1</p>
  <p class="caption caption--red" style="left:622px; top:267px;">Banner 2</p>
  <p class="caption caption--red" style="left:622px; top:563px;">Static style</p>
  <p class="caption caption--dark" style="left:280px; top:818px;">Animated &amp; Static style</p>

  <svg width="0" height="0" style="position:absolute" aria-hidden="true">
    <defs>
      <linearGradient id="header-sheen" x1="0" y1="0" x2="0" y2="1">
        <stop offset="0" stop-color="#ffffff"/>
        <stop offset="0.7" stop-color="#f4f4f4"/>
        <stop offset="1" stop-color="#d6d6d6"/>
      </linearGradient>
      <linearGradient id="swoosh-metal" x1="0" y1="0" x2="1" y2="0">
        <stop offset="0" stop-color="#3c3c3c"/>
        <stop offset="0.35" stop-color="#9a9a9a"/>
        <stop offset="0.5" stop-color="#f2f2f2"/>
        <stop offset="0.65" stop-color="#9a9a9a"/>
        <stop offset="1" stop-color="#3c3c3c"/>
      </linearGradient>
    </defs>
  </svg>

  <!-- Newsletter banner, variant one -->
  <section class="banner" style="left:131px; top:44px;">
    <svg class="banner__top" viewBox="0 0 300 72" aria-hidden="true">
      <path d="M0 0 H300 V66 Q150 40 0 66 Z" fill="#6a6a6a"/>
      <path d="M0 0 H300 V60 Q150 46 0 60 Z" fill="url(#swoosh-metal)"/>
      <path d="M0 0 H300 V56 Q150 36 0 56 Z" fill="url(#header-sheen)"/>
    </svg>
    <h2 class="banner__heading">RECEIVE OUR UPDATE WEEKLY</h2>
    <div class="panel">
      <div class="panel__feature">
        <div class="thumb"><div class="thumb__fill thumb__fill--watch" role="img" aria-label="Photo of a man in a suit adjusting his wristwatch"></div></div>
        <p class="headline">5 ways to look more Professional</p>
      </div>
      <div class="panel__strip"><div class="email-field">Your email address</div></div>
    </div>
    <div class="cta" style="left:80px;">
      <span class="cta__label">SUBMIT NOW</span><span class="cta__divider"></span>
      <svg class="cta__icon" viewBox="0 0 27 27" aria-hidden="true"><circle cx="13.5" cy="13.5" r="12.5" fill="var(--cocoa)" stroke="#f8c27a" stroke-width="1"/><path d="M10.5 7.5 L19 13.5 L10.5 19.5 Z" fill="#f7e2c4"/></svg>
    </div>
  </section>

  <!-- Newsletter banner, variant two -->
  <section class="banner" style="left:131px; top:301px;">
    <svg class="banner__top" viewBox="0 0 300 72" aria-hidden="true">
      <path d="M0 0 H300 V66 Q150 40 0 66 Z" fill="#6a6a6a"/>
      <path d="M0 0 H300 V60 Q150 46 0 60 Z" fill="url(#swoosh-metal)"/>
      <path d="M0 0 H300 V56 Q150 36 0 56 Z" fill="url(#header-sheen)"/>
    </svg>
    <h2 class="banner__heading">RECEIVE OUR UPDATE WEEKLY</h2>
    <div class="panel">
      <div class="panel__feature">
        <div class="thumb" style="left:19px;"><div class="thumb__fill thumb__fill--phone" role="img" aria-label="Photo of a young professional in a dark suit checking a phone"></div></div>
        <p class="headline headline--four">What Interview Questions Should You Know</p>
      </div>
      <div class="panel__strip"><div class="email-field">Your email address</div></div>
    </div>
    <div class="cta" style="left:80px;">
      <span class="cta__label">SUBMIT NOW</span><span class="cta__divider"></span>
      <svg class="cta__icon" viewBox="0 0 27 27" aria-hidden="true"><circle cx="13.5" cy="13.5" r="12.5" fill="var(--cocoa)" stroke="#f8c27a" stroke-width="1"/><path d="M10.5 7.5 L19 13.5 L10.5 19.5 Z" fill="#f7e2c4"/></svg>
    </div>
  </section>

  <!-- Newsletter banner, variant three -->
  <section class="banner" style="left:131px; top:559px;">
    <svg class="banner__top" viewBox="0 0 300 72" aria-hidden="true">
      <path d="M0 0 H300 V66 Q150 40 0 66 Z" fill="#6a6a6a"/>
      <path d="M0 0 H300 V60 Q150 46 0 60 Z" fill="url(#swoosh-metal)"/>
      <path d="M0 0 H300 V56 Q150 36 0 56 Z" fill="url(#header-sheen)"/>
    </svg>
    <h2 class="banner__heading">RECEIVE OUR UPDATE WEEKLY</h2>
    <div class="panel">
      <div class="panel__feature">
        <div class="thumb" style="left:19px;"><div class="thumb__fill thumb__fill--typing" role="img" aria-label="Photo of hands typing on a laptop keyboard"></div></div>
        <p class="headline headline--four">What Your Email Style Says About Your Personality</p>
      </div>
      <div class="panel__strip"><div class="email-field">Your email address</div></div>
    </div>
    <div class="cta" style="left:80px;">
      <span class="cta__label">SUBMIT NOW</span><span class="cta__divider"></span>
      <svg class="cta__icon" viewBox="0 0 27 27" aria-hidden="true"><circle cx="13.5" cy="13.5" r="12.5" fill="var(--cocoa)" stroke="#f8c27a" stroke-width="1"/><path d="M10.5 7.5 L19 13.5 L10.5 19.5 Z" fill="#f7e2c4"/></svg>
    </div>
  </section>

  <!-- Summit banner -->
  <section class="banner" style="left:474px; top:299px;">
    <svg class="banner__top" viewBox="0 0 300 72" aria-hidden="true">
      <path d="M0 0 H300 V66 Q150 40 0 66 Z" fill="#6a6a6a"/>
      <path d="M0 0 H300 V60 Q150 46 0 60 Z" fill="url(#swoosh-metal)"/>
      <path d="M0 0 H300 V56 Q150 36 0 56 Z" fill="url(#header-sheen)"/>
    </svg>
    <h2 class="banner__heading banner__heading--teal">HORIZON SUMMIT</h2>
    <div class="panel">
      <div class="panel__feature">
        <div class="thumb" style="left:3px; top:8px;"><div class="thumb__fill thumb__fill--crowd" role="img" aria-label="Photo of young professionals in suits at a convention"></div></div>
        <p class="lead">Designed to Enhance Young Professionals Abilities To Give Their Best Work</p>
      </div>
      <div class="panel__strip"><p class="strip-title">ONE DAY WORKSHOP<br>CONVENTION</p></div>
    </div>
    <div class="cta" style="left:81px; top:200px;">
      <span class="cta__label">CLICK HERE</span><span class="cta__divider"></span>
      <svg class="cta__icon" viewBox="0 0 27 27" aria-hidden="true"><circle cx="13.5" cy="13.5" r="12.5" fill="var(--cocoa)" stroke="#f8c27a" stroke-width="1"/><path d="M10.5 7.5 L19 13.5 L10.5 19.5 Z" fill="#f7e2c4"/></svg>
    </div>
  </section>

</main>
</body>
</html>
```